Wordpress Corporate Website for New Business

We need a corporate website created which will act as a professional shop window for our new business. We do not need special features like merchant facilities or chatbots. The attachment shows suggested key sections as well as some possible wording. Various versions of the company logo have been attached as well to give different options to play with. We are looking for an option which is easy for us to take over and manage moving forward should we need to make minor updates.

Target Market(s)

Corporate entities

Industry/Entity Type

Private share auctions

Coding

Coded - Design and coding required

```html
<!DOCTYPE html>
<html lang="en">
<head>
<meta charset="utf-8">
<title>TradeMere — Corporate Website</title>
<link rel="stylesheet" href="https://fonts.googleapis.com/css2?family=Lexend:wght@300;400;500;600&display=swap">
<style>
:root{
  --navy:#14009c;
  --purple:#8c0ea3;
  --magenta:#a412bd;
  --ink:#1d1d28;
  --page:#efeff2;
  --footer:#1c1c1f;
  --white:#ffffff;
}
*{margin:0;padding:0;box-sizing:border-box}
html,body{width:1200px;height:2496px;overflow:hidden}
body{background:var(--page);font-family:"Lexend",sans-serif;color:var(--ink);position:relative}
.abs{position:absolute}
.site{position:absolute;background:var(--white);overflow:hidden}
.desktop{left:158px;top:174px;width:547px;height:1414px}
.mobile{left:874px;top:174px;width:176px;height:2170px}

.nav{position:absolute;left:0;top:0;width:100%;background:var(--white);display:flex;align-items:center;z-index:3;box-shadow:0 1px 4px rgba(0,0,0,.06)}
.brand{display:flex;align-items:center;gap:4px;font-weight:600;color:var(--navy)}
.brand-dot{border-radius:50%;background:var(--purple)}
.nav-links{display:flex;gap:13px;font-size:5.2px;color:var(--navy);font-weight:500}
.nav-links .current{color:var(--purple);border-bottom:1px solid var(--purple)}
.pill{position:absolute;display:flex;align-items:center;justify-content:center;border-radius:20px;background:var(--navy);color:var(--white);font-weight:500;white-space:nowrap}
.pill.purple{background:var(--purple)}
.pill.light{background:var(--white);color:var(--navy)}

.hero-photo{position:absolute;left:0;width:100%;background:
  radial-gradient(ellipse at 70% 40%,rgba(160,110,220,.55) 0%,rgba(160,110,220,0) 55%),
  linear-gradient(120deg,#6a2aa8 0%,#8a4fc4 45%,#4d2496 100%)}
.hero-title{position:absolute;left:0;width:100%;text-align:center;color:var(--white);font-weight:500;text-shadow:0 1px 4px rgba(30,0,70,.35)}
.arrow{position:absolute;text-align:center;width:100%}

.h2{position:absolute;font-weight:500;color:var(--navy)}
.h2 em{font-style:normal;color:var(--purple)}
.body{position:absolute;color:#333;font-weight:300}
.feature-photo{position:absolute;border-radius:22px 80px 22px 80px;background:
  radial-gradient(circle at 30% 30%,rgba(255,255,255,.25),rgba(255,255,255,0) 45%),
  linear-gradient(140deg,#b11fd0 0%,#7a10b8 50%,#2a0fb0 100%);box-shadow:0 6px 18px rgba(60,0,120,.18)}

.team-bg{position:absolute;left:0;width:100%;background:linear-gradient(180deg,#f5f5f7 0%,#ececef 55%,#d6d6db 100%)}
.card{position:absolute;background:var(--white);border-radius:8px;box-shadow:0 3px 10px rgba(20,0,80,.10);text-align:center;overflow:hidden}
.card-photo{position:absolute;left:0;top:0;width:100%;background:
  linear-gradient(180deg,rgba(255,255,255,0) 55%,rgba(40,40,60,.28) 100%),
  linear-gradient(115deg,#eef0f3 0%,#cfd4dc 50%,#aeb5c0 100%)}
.card-name{position:absolute;left:0;width:100%;font-weight:500;color:var(--ink)}
.card-role{position:absolute;left:0;width:100%;color:var(--purple);font-weight:300}
.social-dot{position:absolute;border-radius:50%;background:var(--navy);border:2px solid var(--white)}

.band{position:absolute;overflow:hidden;display:flex}
.band-half{position:relative;flex:1;display:flex;align-items:center;justify-content:center}
.band-company{background:linear-gradient(135deg,#2a16d0,#0d0090)}
.band-holder{background:linear-gradient(135deg,#b818d2,#7d0aa3)}
.band-label{border:1px solid rgba(255,255,255,.6);background:rgba(255,255,255,.14);color:var(--white);display:flex;align-items:center;justify-content:center;font-weight:400}

.feature-icon{position:absolute;border-radius:50%;background:var(--purple);display:flex;align-items:center;justify-content:center;color:var(--white);box-shadow:0 2px 6px rgba(140,14,163,.3)}
.feature-icon svg{width:56%;height:56%}
.feature-label{position:absolute;font-size:5.4px;color:var(--ink);font-weight:500;white-space:nowrap}
.hub-ring{position:absolute;border-radius:50%;background:var(--white);box-shadow:0 0 0 7px #f6f6f8,0 3px 12px rgba(0,0,0,.08)}
.hub-core{position:absolute;border-radius:50%;background:var(--white);border:1.5px solid #e6def0;display:flex;align-items:center;justify-content:center;color:var(--navy);font-weight:600}

.footer{position:absolute;left:0;width:100%;color:#e6e6ea}
.f-head{position:absolute;color:var(--white);font-weight:500}
.f-text{position:absolute;color:#d6d6dc;font-weight:300}
.f-ico{position:absolute;color:var(--magenta)}
.f-input{position:absolute;background:var(--white);border-radius:20px;color:#777;display:flex;align-items:center}
.f-social{position:absolute;border-radius:50%;background:#3a3a40}
.f-social.on{background:var(--purple)}
.copy{position:absolute;color:#cfcfd6;font-weight:300}
.copy em{font-style:normal;color:var(--magenta)}
</style>
</head>
<body>

<svg width="0" height="0" style="position:absolute">
  <defs>
    <symbol id="i-control" viewBox="0 0 24 24"><g fill="none" stroke="currentColor" stroke-width="1.8" stroke-linecap="round" stroke-linejoin="round"><rect x="3" y="4" width="18" height="12" rx="1.5"/><path d="M12 16v4M8 20h8"/><path d="M7 13l3-3 3 2 4-4"/></g></symbol>
    <symbol id="i-unlock" viewBox="0 0 24 24"><g fill="none" stroke="currentColor" stroke-width="1.8" stroke-linecap="round" stroke-linejoin="round"><rect x="5" y="11" width="14" height="10" rx="1.5"/><path d="M8 11V7a4 4 0 0 1 7.6-1.8"/><path d="M12 15v2"/></g></symbol>
    <symbol id="i-direct" viewBox="0 0 24 24"><g fill="none" stroke="currentColor" stroke-width="1.8" stroke-linecap="round" stroke-linejoin="round"><path d="M4 8h15M16 5l3 3-3 3"/><path d="M20 16H5M8 13l-3 3 3 3"/></g></symbol>
    <symbol id="i-secure" viewBox="0 0 24 24"><g fill="none" stroke="currentColor" stroke-width="1.8" stroke-linecap="round" stroke-linejoin="round"><path d="M12 3l7 3v5c0 5-3 8-7 10-4-2-7-5-7-10V6z"/><path d="M9 12l2 2 4-4"/></g></symbol>
    <symbol id="i-global" viewBox="0 0 24 24"><g fill="none" stroke="currentColor" stroke-width="1.8"><circle cx="12" cy="12" r="9"/><ellipse cx="12" cy="12" rx="4" ry="9"/><path d="M3 12h18"/></g></symbol>
    <symbol id="i-scale" viewBox="0 0 24 24"><g fill="none" stroke="currentColor" stroke-width="2" stroke-linecap="round"><path d="M6 20v-5M10 20v-9M14 20v-7M18 20V6M4 20.5h16"/></g></symbol>
    <symbol id="i-price" viewBox="0 0 24 24"><g fill="none" stroke="currentColor" stroke-width="1.8" stroke-linejoin="round"><path d="M3 11V4h7l11 11-7 7z"/><circle cx="7.5" cy="7.5" r="1.5"/></g></symbol>
    <symbol id="i-phone" viewBox="0 0 24 24"><path fill="currentColor" d="M6.6 10.8a15 15 0 0 0 6.6 6.6l2.2-2.2a1 1 0 0 1 1-.25 11.4 11.4 0 0 0 3.6.57 1 1 0 0 1 1 1V20a1 1 0 0 1-1 1A17 17 0 0 1 3 4a1 1 0 0 1 1-1h3.5a1 1 0 0 1 1 1c0 1.25.2 2.45.57 3.6a1 1 0 0 1-.25 1z"/></symbol>
    <symbol id="i-mail" viewBox="0 0 24 24"><g fill="none" stroke="currentColor" stroke-width="2.2"><rect x="3" y="5" width="18" height="14" rx="2"/><path d="M3 7l9 6 9-6"/></g></symbol>
    <symbol id="i-pin" viewBox="0 0 24 24"><path fill="currentColor" d="M12 2a7 7 0 0 0-7 7c0 5 7 13 7 13s7-8 7-13a7 7 0 0 0-7-7zm0 9.5A2.5 2.5 0 1 1 12 6.5a2.5 2.5 0 0 1 0 5z"/></symbol>
  </defs>
</svg>

<!-- ================= DESKTOP PAGE ================= -->
<main class="site desktop">
  <header class="nav" style="height:35px;padding-left:58px">
    <div class="brand" style="font-size:14px"><span class="brand-dot" style="width:9px;height:9px"></span>TradeMere</div>
    <nav class="nav-links abs" style="left:186px;top:15px">
      <span class="current">Home</span><span>About</span><span>Our Team</span><span>Key Features</span><span>Why Choose TradeMere</span><span>Support</span>
    </nav>
    <span class="pill" style="left:437px;top:9px;width:51px;height:17px;font-size:5.2px">Contact Us</span>
  </header>

  <section class="hero">
    <div class="hero-photo" role="img" aria-label="Person working on a laptop showing trading charts" style="top:35px;height:230px"></div>
    <svg class="abs" style="left:0;top:0" width="547" height="270" viewBox="0 0 547 270">
      <path d="M0 200 Q273 305 547 200 L547 270 L0 270 Z" fill="#fff"/>
      <path d="M40 226 Q273 318 507 226" fill="none" stroke="#8c0ea3" stroke-width="3"/>
    </svg>
    <h1 class="hero-title" style="top:106px;font-size:19px">Retain Control, Unlock Liquidity</h1>
    <span class="pill light" style="left:239px;top:143px;width:69px;height:15px;font-size:5.2px">Contact Us Today!</span>
    <div class="arrow" style="top:226px;font-size:9px;color:var(--navy)">↓</div>
  </section>

  <section class="welcome">
    <div class="feature-photo" role="img" aria-label="Business team reviewing documents in purple tint" style="left:95px;top:294px;width:170px;height:142px"></div>
    <h2 class="h2" style="left:280px;top:293px;font-size:15.5px">Welcome to <em>TradeMere</em></h2>
    <p class="body" style="left:280px;top:321px;width:180px;font-size:5.3px;line-height:10px">At TradeMere, we empower private companies to take control of their share transactions without the hassle of third-party involvement. Our innovative share exchange platform is designed to connect pre-approved buyers and sellers directly, fostering a secure and efficient environment for trading ownership in private enterprises.</p>
    <span class="pill" style="left:280px;top:396px;width:57px;height:16px;font-size:5.2px">Discover More</span>
  </section>

  <section class="team">
    <div class="team-bg" role="img" aria-label="Soft grey city skyline" style="top:446px;height:304px"></div>
    <h2 class="h2" style="left:0;width:100%;text-align:center;top:477px;font-size:15.5px">Our Talented <em>Team</em></h2>

    <div class="card" style="left:92px;top:507px;width:82px;height:120px">
      <div class="card-photo" role="img" aria-label="Portrait of team member in office" style="height:77px"></div>
      <div class="card-name" style="top:89px;font-size:5.6px">Alden Marsh</div>
      <div class="card-role" style="top:97px;font-size:4.6px">Contrary popular</div>
    </div>
    <div class="card" style="left:186px;top:507px;width:82px;height:120px">
      <div class="card-photo" role="img" aria-label="Portrait of team member in office" style="height:77px"></div>
      <div class="card-name" style="top:89px;font-size:5.6px">R. Whitcombe</div>
      <div class="card-role" style="top:97px;font-size:4.6px">Contrary popular</div>
    </div>
    <div class="card" style="left:280px;top:507px;width:82px;height:120px">
      <div class="card-photo" role="img" aria-label="Portrait of team member in office" style="height:77px"></div>
      <div class="card-name" style="top:89px;font-size:5.6px">Alden Marsh</div>
      <div class="card-role" style="top:97px;font-size:4.6px">Contrary popular</div>
    </div>
    <div class="card" style="left:374px;top:507px;width:82px;height:120px">
      <div class="card-photo" role="img" aria-label="Portrait of team member in office" style="height:77px"></div>
      <div class="card-name" style="top:89px;font-size:5.6px">R. Whitcombe</div>
      <div class="card-role" style="top:97px;font-size:4.6px">Contrary popular</div>
    </div>
    <span class="social-dot" style="left:126px;top:620px;width:14px;height:14px"></span>
    <span class="social-dot" style="left:220px;top:620px;width:14px;height:14px;background:var(--purple)"></span>
    <span class="social-dot" style="left:314px;top:620px;width:14px;height:14px"></span>
    <span class="social-dot" style="left:408px;top:620px;width:14px;height:14px"></span>
    <span class="pill" style="left:245px;top:650px;width:57px;height:15px;font-size:5.2px">View All Team</span>
  </section>

  <section class="band" style="left:92px;top:700px;width:364px;height:100px;border-radius:0 0 18px 0">
    <div class="band-half band-company" role="img" aria-label="Blue tinted office photo"><span class="band-label" style="width:120px;height:40px;font-size:16px">Company</span></div>
    <div class="band-half band-holder" role="img" aria-label="Magenta tinted analyst photo"><span class="band-label" style="width:120px;height:40px;font-size:16px">Shareholder</span></div>
  </section>

  <section class="why">
    <h2 class="h2" style="left:0;width:100%;text-align:center;top:833px;font-size:15.5px">Why Choose <em>TradeMere</em></h2>
    <svg class="abs" style="left:0;top:860px" width="547" height="260" viewBox="0 860 547 260">
      <g fill="none" stroke="#c9b8e0" stroke-width=".8">
        <path d="M206 891 L235 891 L240 898"/><path d="M343 891 L318 891 L312 898"/>
        <path d="M165 956 L193 956"/><path d="M382 956 L354 956"/>
        <path d="M175 1040 L195 1040 L205 1030"/><path d="M373 1040 L353 1040 L343 1030"/>
        <path d="M274 1090 L274 1060"/>
      </g>
      <g fill="#14009c">
        <circle cx="240" cy="898" r="1.6"/><circle cx="312" cy="898" r="1.6"/>
        <circle cx="193" cy="956" r="1.6"/><circle cx="354" cy="956" r="1.6"/>
        <circle cx="205" cy="1030" r="1.6"/><circle cx="343" cy="1030" r="1.6"/>
        <circle cx="274" cy="1060" r="1.6"/>
      </g>
    </svg>
    <div class="hub-ring" style="left:206px;top:910px;width:136px;height:136px"></div>
    <div class="hub-core" style="left:226px;top:930px;width:96px;height:96px;font-size:14px">TradeMere</div>

    <span class="feature-icon" style="left:178px;top:877px;width:28px;height:28px"><svg><use href="#i-control"/></svg></span>
    <span class="feature-label" style="left:131px;top:888px">Retain Control</span>
    <span class="feature-icon" style="left:343px;top:877px;width:28px;height:28px"><svg><use href="#i-unlock"/></svg></span>
    <span class="feature-label" style="left:376px;top:888px">Unlock Liquidity</span>
    <span class="feature-icon" style="left:137px;top:942px;width:28px;height:28px"><svg><use href="#i-direct"/></svg></span>
    <span class="feature-label" style="left:75px;top:953px">Direct Transactions</span>
    <span class="feature-icon" style="left:382px;top:942px;width:28px;height:28px"><svg><use href="#i-secure"/></svg></span>
    <span class="feature-label" style="left:416px;top:953px">Secure and Confidential</span>
    <span class="feature-icon" style="left:147px;top:1026px;width:28px;height:28px"><svg><use href="#i-global"/></svg></span>
    <span class="feature-label" style="left:102px;top:1037px">Global Reach</span>
    <span class="feature-icon" style="left:373px;top:1026px;width:28px;height:28px"><svg><use href="#i-scale"/></svg></span>
    <span class="feature-label" style="left:406px;top:1037px">Scalability</span>
    <span class="feature-icon" style="left:260px;top:1090px;width:28px;height:28px"><svg><use href="#i-price"/></svg></span>
    <span class="feature-label" style="left:0;width:547px;text-align:center;top:1122px">Price Discovery</span>
    <span class="pill" style="left:240px;top:1153px;width:68px;height:16px;font-size:5.2px">Contact Us Today!</span>
  </section>

  <footer class="footer" style="top:1120px;height:294px">
    <svg class="abs" style="left:0;top:0" width="547" height="294" viewBox="0 1120 547 294">
      <defs><linearGradient id="fd" x1="0" y1="0" x2="0" y2="1"><stop offset="0" stop-color="#242428"/><stop offset="1" stop-color="#18181b"/></linearGradient></defs>
      <path d="M0 1264 Q273 1138 547 1264 L547 1414 L0 1414 Z" fill="url(#fd)"/>
      <path d="M62 1236 Q273 1132 485 1236" fill="none" stroke="#8c0ea3" stroke-width="3"/>
    </svg>
    <div class="f-head" style="left:91px;top:148px;font-size:7.5px">Trade Mere</div>
    <svg class="f-ico" style="left:91px;top:169px" width="6" height="6"><use href="#i-phone"/></svg>
    <div class="f-text" style="left:101px;top:168px;font-size:5.8px">+65 9100 4821</div>
    <svg class="f-ico" style="left:91px;top:183px" width="6" height="6"><use href="#i-mail"/></svg>
    <div class="f-text" style="left:101px;top:183px;font-size:4.8px">info@trademere.com</div>
    <svg class="f-ico" style="left:91px;top:197px" width="6" height="6"><use href="#i-pin"/></svg>
    <div class="f-text" style="left:101px;top:197px;width:85px;font-size:4.6px;line-height:8px">58 Harbour Row, Saint Laurent, Quebec, HM-2210</div>
    <span class="f-social" style="left:91px;top:228px;width:12px;height:12px"></span>
    <span class="f-social on" style="left:108px;top:228px;width:12px;height:12px"></span>
    <span class="f-social" style="left:125px;top:228px;width:12px;height:12px"></span>
    <span class="f-social" style="left:142px;top:228px;width:12px;height:12px"></span>
    <div class="copy" style="left:91px;top:266px;font-size:4.8px">© 2023 <em>Trade Mere</em>. All Right Reserved.</div>

    <div class="f-head" style="left:230px;top:148px;font-size:7.5px">Quick Links</div>
    <div class="f-text" style="left:230px;top:168px;font-size:4.8px;line-height:10.2px">Home<br>About<br>Our Team<br>Key Features<br>Why Choose TradeMere<br>Support<br>Contact Us</div>

    <div class="f-head" style="left:327px;top:148px;font-size:7.5px">Subscribe Newsletter</div>
    <div class="f-text" style="left:327px;top:164px;width:110px;font-size:4.8px;line-height:8.5px">Sign up newsletter and get the daily latest updates in yout inbox.</div>
    <div class="f-input" style="left:327px;top:187px;width:129px;height:15px;font-size:4.6px;padding-left:9px">Enter your email ...</div>
    <span class="pill purple" style="left:327px;top:210px;width:51px;height:14px;font-size:5px">Subscribe</span>
  </footer>
</main>

<!-- ================= MOBILE PAGE ================= -->
<main class="site mobile">
  <header class="nav" style="height:37px;padding-left:9px">
    <div class="brand" style="font-size:13px"><span class="brand-dot" style="width:8px;height:8px"></span>TradeMere</div>
    <svg class="abs" style="left:152px;top:13px" width="15" height="11" viewBox="0 0 15 11"><g stroke="#14009c" stroke-width="1.4"><line x1="0" y1="1" x2="15" y2="1"/><line x1="0" y1="5.5" x2="15" y2="5.5"/><line x1="0" y1="10" x2="15" y2="10"/></g></svg>
  </header>

  <section class="hero">
    <div class="hero-photo" role="img" aria-label="Person working on a laptop showing trading charts" style="top:37px;height:195px"></div>
    <svg class="abs" style="left:0;top:0" width="176" height="240" viewBox="0 0 176 240">
      <path d="M0 205 Q88 242 176 205 L176 240 L0 240 Z" fill="#fff"/>
      <path d="M0 211 Q88 248 176 211" fill="none" stroke="#8c0ea3" stroke-width="2.5"/>
    </svg>
    <h1 class="hero-title" style="top:66px;font-size:19px;line-height:24.5px">Retain<br>Control, Unlock<br>Liquidity</h1>
    <span class="pill light" style="left:38px;top:151px;width:100px;height:19px;font-size:8px">Contact Us Today!</span>
    <div class="arrow" style="top:194px;font-size:9px;color:var(--white)">↓</div>
  </section>

  <section class="welcome">
    <div class="feature-photo" role="img" aria-label="Business team reviewing documents in purple tint" style="left:30px;top:248px;width:116px;height:118px;border-radius:18px 60px 18px 60px"></div>
    <h2 class="h2" style="left:0;width:100%;text-align:center;top:380px;font-size:14px">Welcome to <em>TradeMere</em></h2>
    <p class="body" style="left:10px;width:156px;text-align:center;top:406px;font-size:6.3px;line-height:12.6px">At TradeMere, we empower private companies to take control of their share transactions without the hassle of third-party involvement. Our innovative share exchange platform is designed to connect pre-approved buyers and sellers directly, fostering a secure and efficient environment for trading ownership in private enterprises.</p>
    <span class="pill" style="left:46px;top:521px;width:84px;height:19px;font-size:7.5px">Discover More</span>
  </section>

  <section class="team">
    <div class="team-bg" role="img" aria-label="Soft grey city skyline" style="top:562px;height:340px"></div>
    <h2 class="h2" style="left:0;width:100%;text-align:center;top:579px;font-size:14px">Our Talented <em>Team</em></h2>
    <div class="card" style="left:27px;top:615px;width:121px;height:176px">
      <div class="card-photo" role="img" aria-label="Portrait of team member in office" style="height:112px"></div>
      <div class="card-name" style="top:126px;font-size:8px">Alden Marsh</div>
      <div class="card-role" style="top:138px;font-size:6.5px">Contrary popular</div>
    </div>
    <span class="social-dot" style="left:78px;top:781px;width:20px;height:20px"></span>
    <div class="abs" style="left:8px;top:672px;color:var(--navy);font-size:11px">‹</div>
    <div class="abs" style="left:161px;top:672px;color:var(--navy);font-size:11px">›</div>
    <span class="pill" style="left:46px;top:820px;width:84px;height:19px;font-size:7.5px">View All Team</span>
  </section>

  <section class="band" style="left:9px;top:860px;width:159px;height:226px;flex-direction:column;border-radius:0 0 22px 0">
    <div class="band-half band-company" role="img" aria-label="Blue tinted office photo"><span class="band-label" style="width:117px;height:44px;font-size:14px">Company</span></div>
    <div class="band-half band-holder" role="img" aria-label="Magenta tinted analyst photo"><span class="band-label" style="width:117px;height:44px;font-size:14px">Shareholder</span></div>
  </section>

  <section class="why">
    <h2 class="h2" style="left:0;width:100%;text-align:center;top:1105px;font-size:14px;line-height:18px">Why Choose<br><em>TradeMere</em></h2>
    <div class="hub-ring" style="left:13px;top:1155px;width:150px;height:150px"></div>
    <div class="hub-core" style="left:35px;top:1177px;width:106px;height:106px;font-size:15px">TradeMere</div>

    <span class="feature-icon" style="left:8px;top:1330px;width:42px;height:42px"><svg><use href="#i-control"/></svg></span>
    <span class="feature-label" style="left:58px;top:1347px;font-size:8px">Retain Control</span>
    <span class="feature-icon" style="left:8px;top:1380px;width:42px;height:42px"><svg><use href="#i-unlock"/></svg></span>
    <span class="feature-label" style="left:58px;top:1397px;font-size:8px">Unlock Liquidity</span>
    <span class="feature-icon" style="left:8px;top:1431px;width:42px;height:42px"><svg><use href="#i-direct"/></svg></span>
    <span class="feature-label" style="left:58px;top:1448px;font-size:8px">Direct Transactions</span>
    <span class="feature-icon" style="left:8px;top:1481px;width:42px;height:42px"><svg><use href="#i-secure"/></svg></span>
    <span class="feature-label" style="left:58px;top:1498px;font-size:8px">Secure and Confidential</span>
    <span class="feature-icon" style="left:8px;top:1532px;width:42px;height:42px"><svg><use href="#i-global"/></svg></span>
    <span class="feature-label" style="left:58px;top:1549px;font-size:8px">Global Reach</span>
    <span class="feature-icon" style="left:8px;top:1582px;width:42px;height:42px"><svg><use href="#i-scale"/></svg></span>
    <span class="feature-label" style="left:58px;top:1599px;font-size:8px">Scalability</span>
    <span class="feature-icon" style="left:8px;top:1632px;width:42px;height:42px"><svg><use href="#i-price"/></svg></span>
    <span class="feature-label" style="left:58px;top:1649px;font-size:8px">Price Discovery</span>
    <span class="pill" style="left:9px;top:1690px;width:100px;height:20px;font-size:7.5px">Contact Us Today!</span>
  </section>

  <footer class="footer" style="top:1720px;height:450px">
    <svg class="abs" style="left:0;top:0" width="176" height="450" viewBox="0 1720 176 450">
      <path d="M0 1752 Q88 1716 176 1752 L176 2170 L0 2170 Z" fill="#1c1c1f"/>
      <path d="M18 1742 Q88 1712 158 1742" fill="none" stroke="#8c0ea3" stroke-width="2.5"/>
    </svg>
    <div class="f-head" style="left:9px;top:55px;font-size:9px">Trade Mere</div>
    <svg class="f-ico" style="left:9px;top:78px" width="7" height="7"><use href="#i-phone"/></svg>
    <div class="f-text" style="left:24px;top:76px;font-size:8px">+65 9100 4821</div>
    <svg class="f-ico" style="left:9px;top:99px" width="7" height="7"><use href="#i-mail"/></svg>
    <div class="f-text" style="left:24px;top:98px;font-size:6.5px">info@trademere.com</div>
    <svg class="f-ico" style="left:9px;top:119px" width="7" height="7"><use href="#i-pin"/></svg>
    <div class="f-text" style="left:24px;top:118px;width:145px;font-size:6.5px;line-height:12.5px">58 Harbour Row, Saint Laurent, Quebec, HM-2210</div>

    <div class="f-head" style="left:9px;top:158px;font-size:9px">Quick Links</div>
    <div class="f-text" style="left:9px;top:181px;font-size:6.5px;line-height:15.3px">Home<br>Our Team<br>Why Choose TradeMere<br>Contact Us</div>
    <div class="f-text" style="left:109px;top:181px;font-size:6.5px;line-height:15.3px">About<br>Key Features<br>Support</div>

    <div class="f-head" style="left:9px;top:254px;font-size:9px">Subscribe Newsletter</div>
    <div class="f-text" style="left:9px;top:274px;width:160px;font-size:6.5px;line-height:12.8px">Sign up newsletter and get the daily latest updates in yout inbox.</div>
    <div class="f-input" style="left:9px;top:306px;width:159px;height:20px;font-size:6.5px;padding-left:9px">Enter your email ...</div>
    <span class="pill purple" style="left:9px;top:336px;width:67px;height:19px;font-size:7.5px">Subscribe</span>
    <span class="f-social" style="left:42px;top:378px;width:18px;height:18px"></span>
    <span class="f-social on" style="left:67px;top:378px;width:18px;height:18px"></span>
    <span class="f-social" style="left:92px;top:378px;width:18px;height:18px"></span>
    <span class="f-social" style="left:117px;top:378px;width:18px;height:18px"></span>
    <div class="copy" style="left:0;width:176px;text-align:center;top:417px;font-size:6.5px">© 2023 <em>Trade Mere</em>. All Right Reserved.</div>
  </footer>
</main>

</body>
</html>
```